VelloTek needs web site design

We need a web site design for our product called 'VelloTek'. We develop an asset management system that can manage all kind of assets. Currently we have a logo theme and would like to use similar color scheme; the content concept is pretty much in http://tdalwynne.net but the product was called "Kestel Suite" at the time and is now called "VelloTek". Vello means Vast Equipment Ledger Logging Organizer.
Please use generic image for asset (not just bridges) e.g buildings, trucks, powerlines. train, bus, lightrail etc..
Please emphazise on the data management and security, and distributed networking.

the new website address is https://www.vellotek.example/

name on business card

Thomas Dalwynne 555-014-7392
Principal Architect / Software Engineer

Tara Dalwynne 555-018-2641
Software Engineer

Coding

Coded - Design and coding required

Number of Pages Required

1 page

```html
<!DOCTYPE html>
<html lang="en">
<head>
<meta charset="utf-8">
<title>VelloTek Asset Management</title>
<link href="https://fonts.googleapis.com/css2?family=Questrial&family=Oswald:wght@400&display=swap" rel="stylesheet">
<style>
:root{
  --navy:#0c1d86;
  --navy-dark:#0a1870;
  --gold:#d6a53a;
  --gold-light:#e6bd5d;
  --ink:#1c1c3a;
  --text:#6b6b75;
  --line:#e2e2e6;
  --grey-bg:#f1f1f1;
  --white:#ffffff;
}
*{margin:0;padding:0;box-sizing:border-box}
html,body{width:1200px;height:3203px;overflow:hidden}
body{position:relative;background:var(--white);font-family:"Questrial",sans-serif;color:var(--text)}
.abs{position:absolute}
a{color:inherit;text-decoration:none}

/* header */
.site-header{position:absolute;left:0;top:0;width:1200px;height:81px;background:rgba(255,255,255,.9);z-index:5}
.brand{position:absolute;display:flex;align-items:center;gap:10px;color:var(--navy);font-size:30px;letter-spacing:.5px;white-space:nowrap}
.brand-mark{width:30px;height:30px;background:var(--gold);display:inline-block}
.site-header .brand{left:156px;top:20px}
.nav a{position:absolute;top:30px;font-size:13px;color:var(--navy);white-space:nowrap}
.nav a.active{color:var(--gold)}
.header-phone{position:absolute;left:770px;top:28px;font-size:16px;color:var(--gold);display:flex;align-items:center;gap:6px;white-space:nowrap}
.login{position:absolute;left:933px;top:21px;width:109px;height:35px;border:1px solid var(--gold);color:var(--navy);font-size:13px;display:flex;align-items:center;justify-content:center;gap:6px}

/* hero */
.hero{position:absolute;left:0;top:0;width:1200px;height:560px;background:linear-gradient(100deg,#8a6a3a 0%,#b48a4e 25%,#6f6656 55%,#4d4d4b 80%,#3a3b3c 100%)}
.hero-title{position:absolute;left:156px;top:203px;color:var(--white);font-size:28px;line-height:34px}
.hero-sub{position:absolute;left:156px;top:278px;color:var(--white);font-size:17px;line-height:22px}
.btn-gold{position:absolute;background:var(--gold);color:var(--white);font-size:12px;display:flex;align-items:center;justify-content:center}
.hero .btn-gold{left:156px;top:348px;width:128px;height:32px}
.slide-arrow{position:absolute;left:1012px;width:31px;height:31px;border-radius:50%;border:2px solid var(--gold)}
.slide-arrow.filled{background:var(--gold)}
.dot{position:absolute;top:483px;width:12px;height:12px;border-radius:50%;border:2px solid var(--white)}
.dot.on{background:var(--white)}
.hero-badge{position:absolute;left:561px;top:522px;width:78px;height:78px;border-radius:50%;background:var(--white);z-index:3;display:flex;align-items:center;justify-content:center}
.hero-badge span{width:30px;height:30px;background:var(--navy)}

/* headings */
.section-title{position:absolute;left:0;width:1200px;text-align:center;color:var(--navy);font-size:27px}
.section-sub{position:absolute;left:0;width:1200px;text-align:center;font-size:15px;color:var(--text)}

/* why */
.why-item{position:absolute;width:260px;text-align:center;color:var(--navy);font-size:15px;line-height:21px}
.why-item svg{display:block;margin:0 auto 14px}
.carousel-arrow{position:absolute;top:780px}
.btn-outline{position:absolute;border:1px solid var(--gold);color:var(--gold);font-size:12px;display:flex;align-items:center;justify-content:center}

/* about */
.about{position:absolute;left:0;top:999px;width:1200px;height:442px;background:var(--grey-bg)}
.laptop{position:absolute;left:47px;top:75px;width:487px;height:254px;background:linear-gradient(180deg,#2b2b2b 0,#2b2b2b 88%,#c9c9cc 88%,#e9e9ec 100%);border-radius:10px 10px 4px 4px}
.about h2{position:absolute;left:612px;top:74px;color:var(--navy);font-size:28px;font-weight:400;line-height:31px}
.about p{position:absolute;left:612px;top:160px;width:430px;font-size:12.5px;line-height:19.5px}
.about .btn-outline{left:612px;top:334px;width:128px;height:34px}

/* accordion */
.accordion{position:absolute;left:132px;top:1505px;width:935px}
.acc-row{position:absolute;left:0;width:935px;height:53px;border-top:1px solid var(--line);color:var(--navy);font-size:16px;display:flex;align-items:center;padding-left:23px}
.acc-row .toggle{position:absolute;right:12px;top:20px;width:13px;height:13px;border-radius:50%;background:#bdbdc3}
.acc-row .toggle::before,.acc-row .toggle::after{content:"";position:absolute;background:#fff;left:3px;top:6px;width:7px;height:1px}
.acc-row .toggle::after{left:6px;top:3px;width:1px;height:7px}
.acc-row.open .toggle{background:var(--gold)}
.acc-row.open .toggle::after{display:none}
.acc-body{position:absolute;font-size:12.5px;line-height:19px}
.monitor{position:absolute;left:579px;top:124px;width:282px;height:224px}
.feature{position:absolute;width:260px;text-align:center}
.feature h4{color:var(--navy);font-size:14px;font-weight:400;margin:10px 0 4px}
.feature p{font-size:12px;line-height:19px}
.acc-end{position:absolute;left:0;top:861px;width:935px;border-top:1px solid var(--line)}

/* team */
.team-wave{position:absolute;left:0;top:2540px;width:1200px;height:663px}
.member{position:absolute;top:2509px;width:280px;height:358px;background:#f3f3f5}
.member .photo{width:280px;height:277px;background:linear-gradient(180deg,#d7d9dc,#b9bcc0)}
.member .pin{position:absolute;left:130px;top:268px;width:20px;height:20px;border-radius:50%;background:#fff;border:2px solid var(--gold)}
.member h5{text-align:center;margin-top:26px;color:var(--navy);font-size:14px;font-weight:400}
.member span{display:block;text-align:center;font-size:12px;margin-top:4px}

/* footer */
.site-footer .brand{left:0;width:1200px;justify-content:center;top:2933px;color:var(--gold);font-size:32px}
.footer-nav{position:absolute;left:0;top:2998px;width:1200px;display:flex;justify-content:center;gap:28px;color:var(--white);font-size:12px}
.footer-nav .sep{opacity:.8}
.footer-nav .active{color:var(--gold)}
.call{position:absolute;left:0;top:3041px;width:1200px;text-align:center;color:var(--gold);font-family:"Oswald",sans-serif;font-size:24px}
.mail{position:absolute;left:0;top:3080px;width:1200px;text-align:center;color:var(--white);font-size:13px;text-decoration:underline}
.footer-rule{position:absolute;left:178px;top:3134px;width:844px;border-top:1px solid rgba(255,255,255,.25)}
.copy{position:absolute;left:180px;top:3160px;color:var(--white);font-size:12px}
.copy b{font-weight:400;color:var(--gold)}
.footer-pin{position:absolute;left:1000px;top:3156px}
</style>
</head>
<body>

<section class="hero" role="img" aria-label="Photo of a long concrete viaduct at sunset, representing infrastructure assets">
  <h1 class="hero-title" style="font-weight:400">We develop an<br>asset management system</h1>
  <p class="hero-sub">We have over 20 years of experience designing, creating<br>and supporting software for professionals.</p>
  <a class="btn-gold">Get Started</a>
  <span class="slide-arrow" style="top:258px"></span>
  <span class="slide-arrow filled" style="top:302px"></span>
  <svg class="abs" style="left:1022px;top:267px" width="12" height="12" viewBox="0 0 12 12"><path d="M8 2L4 6l4 4" fill="none" stroke="#d6a53a" stroke-width="2"/></svg>
  <svg class="abs" style="left:1022px;top:311px" width="12" height="12" viewBox="0 0 12 12"><path d="M4 2l4 4-4 4" fill="none" stroke="#fff" stroke-width="2"/></svg>
  <span class="dot on" style="left:158px"></span>
  <span class="dot" style="left:188px"></span>
</section>

<header class="site-header">
  <div class="brand"><span class="brand-mark"></span>VelloTek</div>
  <nav class="nav">
    <a class="active" style="left:471px">Home</a>
    <a style="left:544px">About Us</a>
    <a style="left:642px">Contact Us</a>
  </nav>
  <div class="header-phone">
    <svg width="14" height="14" viewBox="0 0 24 24"><path fill="#d6a53a" d="M6.6 10.8a15 15 0 006.6 6.6l2.2-2.2c.3-.3.7-.4 1-.2 1.1.4 2.3.6 3.6.6.6 0 1 .4 1 1V20c0 .6-.4 1-1 1A17 17 0 013 4c0-.6.4-1 1-1h3.5c.6 0 1 .4 1 1 0 1.3.2 2.5.6 3.6.1.3 0 .7-.2 1z"/></svg>
    555-014-7392
  </div>
  <a class="login">
    <svg width="11" height="11" viewBox="0 0 12 12"><circle cx="6" cy="3.5" r="2.5" fill="#0c1d86"/><path d="M1 12c0-3 2.2-5 5-5s5 2 5 5z" fill="#0c1d86"/></svg>Login
  </a>
</header>

<div class="hero-badge"><span></span></div>

<!-- why choose us -->
<h2 class="section-title" style="top:636px;font-weight:400">Why choose us</h2>
<p class="section-sub" style="top:674px">Vast Equipment Ledger Logging Organizer</p>

<svg class="carousel-arrow" style="left:120px" width="12" height="22" viewBox="0 0 12 22"><path d="M10 2L2 11l8 9" fill="none" stroke="#9a9aa3" stroke-width="1.5"/></svg>
<svg class="carousel-arrow" style="left:1066px" width="12" height="22" viewBox="0 0 12 22"><path d="M2 2l8 9-8 9" fill="none" stroke="#d6a53a" stroke-width="1.5"/></svg>

<div class="why-item" style="left:167px;top:726px">
  <svg width="70" height="66" viewBox="0 0 70 66" fill="none" stroke="#8a8a92" stroke-width="1.4"><circle cx="42" cy="22" r="12"/><circle cx="42" cy="22" r="5"/><path d="M42 6v-4M42 42v-4M26 22h-4M62 22h-4M30 10l-3-3M57 37l-3-3M30 34l-3 3M57 7l-3 3"/><path d="M8 64V46c0-6 4-9 10-9s10 3 10 9v18"/><circle cx="18" cy="28" r="6"/></svg>
  Software project<br>management
</div>
<div class="why-item" style="left:470px;top:726px">
  <svg width="70" height="66" viewBox="0 0 70 66" fill="none" stroke="#d6a53a" stroke-width="1.6"><rect x="12" y="6" width="46" height="36" rx="2"/><path d="M26 50h18M35 42v8"/><path d="M28 18l-6 6 6 6M42 18l6 6-6 6M37 16l-4 16"/><rect x="18" y="54" width="34" height="6"/></svg>
  Software<br>development
</div>
<div class="why-item" style="left:773px;top:726px">
  <svg width="70" height="66" viewBox="0 0 70 66" fill="none" stroke="#8a8a92" stroke-width="1.4"><rect x="22" y="4" width="42" height="30"/><path d="M30 26l8-8 6 5 10-11"/><circle cx="14" cy="20" r="6"/><path d="M4 62V38c0-5 4-8 10-8l10 2 6-6M14 62V46"/></svg>
  Software training and<br>assistance
</div>

<a class="btn-outline" style="left:536px;top:903px;width:128px;height:34px">Contact Us</a>

<!-- about -->
<section class="about">
  <div class="laptop" role="img" aria-label="Laptop showing the asset inspection software with a data grid and building photo"></div>
  <h2>Experience you can count on<br>who are we?</h2>
  <p>Dalwynne and Associates is a software development firm since 1989, specializing in structural engineering applications, complex database systems, distributed information systems and web base information systems. Our team of experts has significant experience in a wide range of computing architectures, operating systems, database engines, embedded systems and networking systems. Our goal is to simplify complex computing systems so our clients can improve productivity and concentrate on their business problems.</p>
  <a class="btn-outline">Discover More</a>
</section>

<!-- accordion -->
<section class="accordion">
  <div class="acc-row" style="top:0">VelloTek<span class="toggle"></span></div>
  <div class="acc-row open" style="top:53px">Integragted Systems<span class="toggle"></span></div>
  <p class="acc-body" style="left:23px;top:144px;width:520px">The VelloTek application shell provides a unified interface for inspectors, inventory managers and repair list managers. A structure oriented user interface with historical data has been developed over many years of work with real inspectors from many organizations.<br><br>Our design philosophy is to give as full control to the inspector as possible while entering data and check the data after the inspector submits it to be part of the permanent record. In this way inspectors can use the application with little or no training while maintaining the integrity of the database.</p>
  <div class="monitor" role="img" aria-label="Desktop monitor showing the inspection data application" style="background:linear-gradient(180deg,#1d1d1d 0,#1d1d1d 74%,#d7d7da 74%,#d7d7da 82%,transparent 82%),radial-gradient(ellipse at 50% 100%,#d0d0d4 0,#d0d0d4 35%,transparent 36%)"></div>
  <p class="acc-body" style="left:23px;top:384px;width:860px">In addition to the NBI inspection data required additional operational information is supported, such as required repairs, issues, type of inspections performed, how often each inspection type needs to be performed, As Built drawing, notes, documents, and scanned images. With this information, inspections can be scheduled, list of repairs published and bridge information can be publish for general use.</p>

  <div class="feature" style="left:35px;top:487px">
    <svg width="30" height="32" viewBox="0 0 30 32" fill="none" stroke="#8a8a92" stroke-width="1.3"><rect x="2" y="5" width="26" height="25"/><path d="M2 12h26M8 2v6M22 2v6M7 17h4M13 17h4M19 17h4M7 23h4M13 23h4"/></svg>
    <h4>VelloTek Scheduling</h4>
    <p>Create and manipulate inspection trip<br>schedules.</p>
  </div>
  <div class="feature" style="left:338px;top:487px">
    <svg width="30" height="32" viewBox="0 0 30 32" fill="none" stroke="#8a8a92" stroke-width="1.3"><rect x="3" y="2" width="24" height="28"/><path d="M8 9h14M8 14h10M8 19h6M14 27l10-12 3 3-10 12h-3z"/></svg>
    <h4>VelloTek Repair List</h4>
    <p>Extract and manage list of repairs of<br>bridge structures.</p>
  </div>
  <div class="feature" style="left:611px;top:487px">
    <svg width="32" height="32" viewBox="0 0 32 32" fill="none" stroke="#8a8a92" stroke-width="1.3"><path d="M4 28l14-14M8 4a6 6 0 008 8l12 12-4 4-12-12a6 6 0 01-8-8l4 4 4-4z"/><path d="M20 4l8 8-3 3-8-8z"/></svg>
    <h4>Web Publishing</h4>
    <p>Bridge information for other departments<br>and general public on the Web.</p>
  </div>

  <div class="acc-row" style="top:650px">Configuration Editor<span class="toggle"></span></div>
  <div class="acc-row" style="top:703px">Centralized Data and Distributed Information<span class="toggle"></span></div>
  <div class="acc-row" style="top:755px">FHWA Compliance for the National Bridge Inventory (NBI)<span class="toggle"></span></div>
  <div class="acc-row" style="top:808px">Emergency Response Support<span class="toggle"></span></div>
  <div class="acc-end"></div>
</section>

<!-- team -->
<h2 class="section-title" style="top:2421px;font-weight:400">Talented team</h2>
<p class="section-sub" style="top:2458px">Vast Equipment Ledger Logging Organizer</p>

<svg class="team-wave" viewBox="0 0 1200 663" preserveAspectRatio="none"><path d="M0 80C160 40 300 60 420 110 560 165 760 130 900 70 1020 20 1120 0 1200 0V663H0z" fill="#0c1d86"/></svg>

<div class="member" style="left:307px">
  <div class="photo" role="img" aria-label="Portrait photo of Thomas Dalwynne"></div>
  <span class="pin"></span>
  <h5>Thomas Dalwynne</h5>
  <span>Software Engineer</span>
</div>
<div class="member" style="left:613px">
  <div class="photo" role="img" aria-label="Portrait photo of Tara Dalwynne"></div>
  <span class="pin"></span>
  <h5>Tara Dalwynne</h5>
  <span>Software Engineer</span>
</div>

<!-- footer -->
<footer class="site-footer">
  <div class="brand"><span class="brand-mark" style="background:var(--white)"></span>VelloTek</div>
  <nav class="footer-nav">
    <a class="active">Home</a><span class="sep">|</span>
    <a>About Us</a><span class="sep">|</span>
    <a>Portfolio</a><span class="sep">|</span>
    <a>Download</a><span class="sep">|</span>
    <a>Contact Us</a>
  </nav>
  <div class="call">Call Us &#9742; 555-014-7392</div>
  <div class="mail">support@tdalwynne.net</div>
  <div class="footer-rule"></div>
  <p class="copy">© 2018 <b>VelloTek Asset Management</b>. All Right Reserved</p>
  <svg class="footer-pin" width="18" height="24" viewBox="0 0 18 24"><path d="M9 0a9 9 0 00-9 9c0 7 9 15 9 15s9-8 9-15a9 9 0 00-9-9z" fill="#d6a53a"/><circle cx="9" cy="9" r="3.5" fill="#0c1d86"/></svg>
</footer>

</body>
</html>
```